Business Cards

I'd like help creating business cards with the full logo "Veltrona Capital Partners" on the back of the card (navy background with white writing), and abbreviated logo "VCP" on the front. Would like to list name, title, phone number, email, and website listed on front of card. Would like to keep very simple. Front font Arial or similar.

```html
<!DOCTYPE html>
<html lang="en">
<head>
<meta charset="utf-8">
<title>Veltrona Capital Partners – Business Cards</title>
<link rel="stylesheet" href="https://fonts.googleapis.com/css2?family=Arimo:wght@400;700&display=swap">
<style>
  :root {
    --navy: #203669;
    --white: #ffffff;
    --stage: #2c4a33;
    --pattern-light: #f4f4f8;
    --pattern-mid: #e6e6ef;
  }
  * { margin: 0; padding: 0; box-sizing: border-box; }
  html, body {
    width: 1200px;
    height: 1000px;
    overflow: hidden;
  }
  body {
    background: var(--stage);
    font-family: "Arimo", Arial, sans-serif;
    color: var(--navy);
    position: relative;
  }
  .card {
    position: absolute;
    left: 250px;
    width: 700px;
    height: 400px;
    background: var(--white);
    overflow: hidden;
    box-shadow: 0 10px 28px rgba(0,0,0,0.35);
  }

  /* Back of card */
  .card-back { top: 50px; }
  .card-back .pattern-area {
    position: absolute;
    inset: 0;
    background: radial-gradient(ellipse at center, var(--pattern-light) 0%, var(--pattern-mid) 100%);
  }
  .card-back .wordmark {
    position: absolute;
    inset: 0;
    display: flex;
    align-items: center;
    justify-content: center;
    gap: 16px;
  }
  .wordmark-square {
    width: 22px;
    height: 22px;
    background: var(--navy);
  }
  .wordmark-name {
    font-size: 40px;
    font-weight: 700;
    color: var(--navy);
    letter-spacing: 1px;
  }

  /* Front of card */
  .card-front { top: 530px; }
  .front-panel {
    position: absolute;
    left: 0;
    top: 0;
    width: 290px;
    height: 352px;
    background: var(--navy);
    display: flex;
    align-items: center;
    justify-content: center;
    padding-top: 120px;
  }
  .front-monogram {
    font-size: 64px;
    font-weight: 700;
    color: var(--white);
    letter-spacing: 2px;
  }
  .front-band {
    position: absolute;
    left: 290px;
    right: 0;
    bottom: 0;
    height: 48px;
    background: var(--navy);
  }
  .identity {
    position: absolute;
    left: 335px;
    top: 52px;
  }
  .identity-name {
    font-size: 30px;
    font-weight: 700;
    line-height: 1.1;
  }
  .identity-title {
    font-size: 14px;
    font-weight: 700;
    margin-top: 4px;
    padding-left: 8px;
  }
  .contact-list {
    position: absolute;
    left: 380px;
    top: 232px;
    list-style: none;
  }
  .contact-item {
    display: flex;
    align-items: center;
    gap: 12px;
    font-size: 15px;
    font-weight: 700;
    height: 30px;
  }
  .contact-item svg {
    width: 20px;
    height: 20px;
    flex: none;
  }
</style>
</head>
<body>

  <section class="card card-back" aria-label="Back of business card">
    <div class="pattern-area" role="img" aria-label="Light hexagon grid background pattern"></div>
    <div class="wordmark">
      <span class="wordmark-square"></span>
      <span class="wordmark-name">Veltrona Capital Partners</span>
    </div>
  </section>

  <section class="card card-front" aria-label="Front of business card">
    <div class="front-panel">
      <span class="front-monogram">VCP</span>
    </div>
    <div class="front-band"></div>

    <div class="identity">
      <h1 class="identity-name">Noel Varden</h1>
      <p class="identity-title">Co-Founder &amp; Managing Partner</p>
    </div>

    <ul class="contact-list">
      <li class="contact-item">
        <svg viewBox="0 0 24 24" fill="none" stroke="currentColor" stroke-width="1.8" stroke-linejoin="round">
          <path d="M5 3h4l2 5-2.5 1.5a11 11 0 0 0 6 6L16 13l5 2v4a2 2 0 0 1-2 2A16 16 0 0 1 3 5a2 2 0 0 1 2-2z"/>
        </svg>
        <span>555-204-7318</span>
      </li>
      <li class="contact-item">
        <svg viewBox="0 0 24 24" fill="none" stroke="currentColor" stroke-width="1.8" stroke-linejoin="round">
          <rect x="3" y="5" width="18" height="14"/>
          <path d="M3 5l9 8 9-8"/>
        </svg>
        <span>noel@veltronacp.com</span>
      </li>
      <li class="contact-item">
        <svg viewBox="0 0 24 24" fill="none" stroke="currentColor" stroke-width="1.8">
          <circle cx="12" cy="12" r="9"/>
          <ellipse cx="12" cy="12" rx="4" ry="9"/>
          <path d="M3 12h18M5 7h14M5 17h14"/>
        </svg>
        <span>www.veltronacp.com</span>
      </li>
    </ul>
  </section>

</body>
</html>
```